Manuka honey wholesales and exports

We need business cards for our honey distribution company based in New Zealand. We supply shops locally and export Manuka honey around the world.
We deal with a very high quality and 100% natural product that can be used for medical, general health as well as food. We are looking business cards that show our honey products are of a high quality with a modern look.

Target Market(s)

Health and medical retailers and importers

Industry/Entity Type

Wholesale

Contact Information for Business Card

Kestrel Hive NZ Limited

www.kestrelhivenz.com

Gareth Moffat

M +64 213958264

E kestrelhivenz@mailbox-example.com

PO Box 47-518
Takapuna
North Shore
Auckland
New Zealand

Font styles to use
Serif

Requirements
Must have
• (Kestrel Hive NZ Limited) with some artwork on one side and all details on the other side.
Nice to have
• I have seen a very simple card with large yellow and black stripes on one side with a company name.. looked clean and simple so something similar or just let the creative beast inside you take over and we will see what you can come up with.

```html
<!DOCTYPE html>
<html lang="en">
<head>
<meta charset="utf-8">
<title>Kestrel Hive NZ Limited – Business Cards</title>
<link rel="stylesheet" href="https://fonts.googleapis.com/css2?family=Tinos&display=swap">
<style>
  :root {
    --honey: #f2ea1b;
    --ink: #0d0d0d;
    --backdrop: #7a624a;
    --ink-soft: rgba(13,13,13,0.42);
    --honey-soft: rgba(242,234,27,0.5);
  }
  * { margin: 0; padding: 0; box-sizing: border-box; }
  html, body { width: 1000px; height: 1200px; overflow: hidden; }
  body {
    position: relative;
    background: var(--backdrop);
    font-family: "Tinos", "Times New Roman", serif;
  }
  .card {
    position: absolute;
    left: 98px;
    width: 810px;
    height: 474px;
    box-shadow: 0 6px 18px rgba(0,0,0,0.45);
  }
  .card--front { top: 102px; background: var(--honey); color: var(--ink); }
  .card--back  { top: 633px; background: var(--ink); color: var(--honey); }
  .card__frame { position: absolute; inset: 0; width: 100%; height: 100%; }

  /* Ornamental flourish area surrounding the company name */
  .ornament {
    position: absolute;
    transform: translate(-50%, -50%);
    border-radius: 50%;
  }
  .card--front .ornament {
    left: 220px; top: 236px;
    width: 352px; height: 306px;
    background: radial-gradient(ellipse at center, var(--ink-soft) 0%, rgba(13,13,13,0.22) 55%, rgba(13,13,13,0) 72%);
  }
  .card--back .ornament {
    left: 405px; top: 237px;
    width: 420px; height: 360px;
    background: radial-gradient(ellipse at center, var(--honey-soft) 0%, rgba(242,234,27,0.24) 55%, rgba(242,234,27,0) 72%);
  }

  .brand {
    position: absolute;
    display: flex;
    flex-direction: column;
    align-items: center;
    gap: 12px;
    transform: translate(-50%, -50%);
    white-space: nowrap;
    text-align: center;
  }
  .brand__dot {
    border-radius: 50%;
    background: currentColor;
    flex: none;
  }
  .brand__name {
    line-height: 1.12;
    letter-spacing: 2px;
    text-transform: uppercase;
  }
  .card--front .brand { left: 220px; top: 236px; }
  .card--front .brand__dot { width: 56px; height: 56px; }
  .card--front .brand__name { font-size: 25px; }
  .card--back .brand { left: 405px; top: 237px; }
  .card--back .brand__dot { width: 66px; height: 66px; }
  .card--back .brand__name { font-size: 30px; }

  .divider {
    position: absolute;
    left: 427px; top: 126px;
    width: 1.5px; height: 222px;
    background: rgba(13,13,13,0.55);
  }
  .details { position: absolute; left: 453px; top: 139px; }
  .details__name { font-size: 29px; font-weight: 400; line-height: 1; }
  .details__role { font-size: 17px; margin-top: 10px; }
  .details__address { font-size: 17px; line-height: 24px; margin-top: 14px; font-style: normal; }
  .contact { list-style: none; margin-top: 11px; }
  .contact__item {
    display: flex; align-items: center; gap: 9px;
    font-size: 17px; height: 25px;
  }
  .contact__icon { width: 17px; height: 17px; flex: none; }
</style>
</head>
<body>

<section class="card card--front" aria-label="Card front">
  <svg class="card__frame" viewBox="0 0 810 474" aria-hidden="true">
    <g fill="none" stroke="var(--ink)" stroke-width="2">
      <rect x="29" y="28" width="752" height="418"/>
      <rect x="35" y="34" width="740" height="406"/>
    </g>
    <g fill="var(--ink)">
      <rect x="32" y="31" width="20" height="20"/>
      <rect x="758" y="31" width="20" height="20"/>
      <rect x="32" y="423" width="20" height="20"/>
      <rect x="758" y="423" width="20" height="20"/>
    </g>
  </svg>

  <div class="ornament" role="img" aria-label="Symmetrical black leaf-and-scroll flourish framing the company name"></div>
  <div class="brand">
    <span class="brand__dot" aria-hidden="true"></span>
    <span class="brand__name">Kestrel Hive<br>NZ Limited</span>
  </div>

  <div class="divider" aria-hidden="true"></div>

  <div class="details">
    <h1 class="details__name">Gareth Moffat</h1>
    <p class="details__role">Owner</p>
    <address class="details__address">PO Box 47-518, Takapuna, North Shore<br>Auckland, New Zealand</address>
    <ul class="contact">
      <li class="contact__item">
        <svg class="contact__icon" viewBox="0 0 20 20" aria-hidden="true"><circle cx="10" cy="10" r="10" fill="var(--ink)"/><path d="M6.5 5.5l2 0.3 0.8 2.3-1.2 1a6 6 0 0 0 2.8 2.8l1-1.2 2.3 0.8 0.3 2-1.5 1.2c-3.8-0.4-7.2-3.8-7.6-7.6z" fill="var(--honey)"/></svg>
        <span>+64 213958264</span>
      </li>
      <li class="contact__item">
        <svg class="contact__icon" viewBox="0 0 20 20" aria-hidden="true"><circle cx="10" cy="10" r="10" fill="var(--ink)"/><rect x="5" y="6.5" width="10" height="7" fill="none" stroke="var(--honey)" stroke-width="1.3"/><path d="M5 6.5l5 4 5-4" fill="none" stroke="var(--honey)" stroke-width="1.3"/></svg>
        <span>kestrelhivenz@mailbox-example.com</span>
      </li>
      <li class="contact__item">
        <svg class="contact__icon" viewBox="0 0 20 20" aria-hidden="true"><circle cx="10" cy="10" r="10" fill="var(--ink)"/><g fill="none" stroke="var(--honey)" stroke-width="1.1"><circle cx="10" cy="10" r="5"/><ellipse cx="10" cy="10" rx="2.2" ry="5"/><path d="M5 10h10"/></g></svg>
        <span>www.kestrelhivenz.com</span>
      </li>
    </ul>
  </div>
</section>

<section class="card card--back" aria-label="Card back">
  <svg class="card__frame" viewBox="0 0 810 474" aria-hidden="true">
    <g fill="none" stroke="var(--honey)" stroke-width="2">
      <rect x="29" y="35" width="752" height="410"/>
      <rect x="35" y="41" width="740" height="398"/>
    </g>
    <g fill="var(--honey)">
      <rect x="32" y="38" width="20" height="20"/>
      <rect x="758" y="38" width="20" height="20"/>
      <rect x="32" y="422" width="20" height="20"/>
      <rect x="758" y="422" width="20" height="20"/>
    </g>
  </svg>

  <div class="ornament" role="img" aria-label="Symmetrical yellow leaf-and-scroll flourish framing the company name"></div>
  <div class="brand">
    <span class="brand__dot" aria-hidden="true"></span>
    <span class="brand__name">Kestrel Hive<br>NZ Limited</span>
  </div>
</section>

</body>
</html>
```